TalkBridge - Language Coaching Services

Sleek, innovative, trendy design for Language Coaching business.

TalkBridge is a new UK based company that provides Language Coaching services. We offer highly personalized on-line and face to face language courses. We also impart learning techniques workshops based on the latest neuroscience research for second-language acquisition.

Target Market(s)

Industry/Entity Type

Consulting

Contact Information for Business Card

TalkBridge
ElenaVT@talkbridge-demo.co.uk
TalkBridge-demo.co.uk
London, UK

Font styles to use
Sans Serif

```html
<!DOCTYPE html>
<html lang="en">
<head>
<meta charset="utf-8">
<title>TalkBridge – Business Card</title>
<link rel="stylesheet" href="https://fonts.googleapis.com/css2?family=Lato:wght@400;700&display=swap">
<style>
  :root {
    --page-bg: #efede9;
    --blue-light: #0a9bd8;
    --blue-dark: #175a85;
    --blue-brand: #1d8ecb;
    --white: #ffffff;
    --text-grey: #7a7a7a;
    --ghost: #e5ecf2;
  }
  * { box-sizing: border-box; margin: 0; padding: 0; }
  html, body {
    width: 1200px; height: 1000px; overflow: hidden;
    background: var(--page-bg);
    font-family: "Lato", sans-serif;
  }
  .canvas { position: relative; width: 1200px; height: 1000px; }

  .card {
    position: absolute; left: 293px; width: 614px;
    overflow: hidden;
    box-shadow: 0 6px 14px rgba(0,0,0,0.25);
  }
  .card--front {
    top: 66px; height: 402px;
    background: linear-gradient(90deg, var(--blue-light) 0%, #1477ad 55%, var(--blue-dark) 100%);
  }
  .card--back { top: 523px; height: 404px; background: var(--white); }

  /* Front */
  .front-mark {
    position: absolute; left: 43px; top: 123px; width: 156px; height: 156px;
    border: 8px solid var(--white); border-radius: 50%;
  }
  .front-name {
    position: absolute; left: 43px; top: 189px; width: 156px;
    text-align: center; color: var(--white);
    font-weight: 700; font-size: 21px;
  }
  .services {
    position: absolute; left: 233px; top: 113px; list-style: none;
  }
  .services li {
    display: flex; align-items: center; height: 29.6px;
    color: var(--white); font-size: 17px; font-weight: 400;
  }
  .services svg { width: 16px; height: 16px; margin-right: 8px; flex: none; }

  /* Back */
  .ghost-ring {
    position: absolute; left: 381px; top: 32px; width: 234px; height: 234px;
    border: 14px solid var(--ghost); border-radius: 50%;
  }
  .ghost-name {
    position: absolute; left: 381px; top: 133px; width: 234px;
    text-align: center; color: var(--ghost);
    font-weight: 700; font-size: 30px;
  }
  .brand-mark {
    position: absolute; left: 111px; top: 43px; width: 92px; height: 92px;
    border: 6px solid var(--blue-brand); border-radius: 50%;
  }
  .brand-name {
    position: absolute; left: 44px; top: 136px;
    color: var(--blue-brand); font-weight: 700;
    font-size: 34px; letter-spacing: 1px;
  }
  .person-name {
    position: absolute; left: 44px; top: 212px;
    color: var(--blue-brand); font-weight: 700; font-size: 20px;
  }
  .contacts { position: absolute; left: 44px; top: 254px; list-style: none; }
  .contacts li {
    display: flex; align-items: center; height: 30px;
    color: var(--text-grey); font-size: 17px;
  }
  .contacts svg { width: 19px; height: 19px; margin-right: 9px; flex: none; }
  .band {
    position: absolute; left: 0; bottom: 0; width: 100%; height: 47px;
    background: linear-gradient(90deg, var(--blue-light) 0%, #1477ad 55%, var(--blue-dark) 100%);
  }
</style>
</head>
<body>
<main class="canvas">

  <section class="card card--front" aria-label="Business card front">
    <div class="front-mark"></div>
    <div class="front-name">TalkBridge</div>
    <ul class="services">
      <li><svg viewBox="0 0 16 16"><path d="M2 9l4 4 8-10" fill="none" stroke="#fff" stroke-width="2.6" stroke-linecap="round" stroke-linejoin="round"/></svg>Face to Face language coaching classes</li>
      <li><svg viewBox="0 0 16 16"><path d="M2 9l4 4 8-10" fill="none" stroke="#fff" stroke-width="2.6" stroke-linecap="round" stroke-linejoin="round"/></svg>Online language coaching sessions</li>
      <li><svg viewBox="0 0 16 16"><path d="M2 9l4 4 8-10" fill="none" stroke="#fff" stroke-width="2.6" stroke-linecap="round" stroke-linejoin="round"/></svg>Personalized Newsletters for self-learners</li>
      <li><svg viewBox="0 0 16 16"><path d="M2 9l4 4 8-10" fill="none" stroke="#fff" stroke-width="2.6" stroke-linecap="round" stroke-linejoin="round"/></svg>Language Learning Techniques Workshops</li>
      <li><svg viewBox="0 0 16 16"><path d="M2 9l4 4 8-10" fill="none" stroke="#fff" stroke-width="2.6" stroke-linecap="round" stroke-linejoin="round"/></svg>Mindful Learning Workshops</li>
      <li><svg viewBox="0 0 16 16"><path d="M2 9l4 4 8-10" fill="none" stroke="#fff" stroke-width="2.6" stroke-linecap="round" stroke-linejoin="round"/></svg>Access to premium content, resources</li>
    </ul>
  </section>

  <section class="card card--back" aria-label="Business card back">
    <div class="ghost-ring"></div>
    <div class="ghost-name">TalkBridge</div>
    <div class="brand-mark"></div>
    <div class="brand-name">TALKBRIDGE</div>
    <div class="person-name">ELENA VT</div>
    <ul class="contacts">
      <li><svg viewBox="0 0 20 20"><rect x="1" y="4" width="18" height="12" fill="#1e6f9f"/><path d="M1 4l9 7 9-7" fill="none" stroke="#fff" stroke-width="1.5"/></svg>ElenaVT@talkbridge-demo.co.uk</li>
      <li><svg viewBox="0 0 20 20"><circle cx="10" cy="10" r="8.5" fill="none" stroke="#1e6f9f" stroke-width="2"/><ellipse cx="10" cy="10" rx="3.5" ry="8.5" fill="none" stroke="#1e6f9f" stroke-width="1.6"/><path d="M1.5 10h17" stroke="#1e6f9f" stroke-width="1.6"/></svg>TalkBridge-demo.co.uk</li>
      <li><svg viewBox="0 0 20 20"><path d="M10 19s-6-6.5-6-11a6 6 0 0 1 12 0c0 4.5-6 11-6 11z" fill="#1e8fcb"/><circle cx="10" cy="8" r="2.3" fill="#fff"/></svg>London, UK</li>
    </ul>
    <div class="band"></div>
  </section>

</main>
</body>
</html>
```